Price Package PDF - 2 page PDF of stylized price packages for property management firm

Looking for a 2 x A4 page PDF for our two price packages.
I would like this to be in similar style to our website www.harbourlanerentals.com.au
I have attached an example. But would like mine to be a little more stylish and modern, preferably using design similar to our website.
Words and images also attached

Target Market(s)

investment property owners, male and female, aged 30-60

Industry/Entity Type

Real Estate

Font styles to use
Sans Serif

Requirements
Must have
• split two packages onto seperate A4 pages (See example file attached)
• Contact info:
• Website: www.harbourlanerentals.com.au
• email: info@harbourlanerentals.com.au
• Phone: Tom Willard 0438 216 907, Marika Dunstan 0419 572 046
• Office Address: Suite 7, 12-14 Carrow Parade, Dee Why NSW 2099
Nice to have
• I would like to use any of the pictures provided or images of modern residential property interior or of Sydney's Northern Beaches.

```html
<!DOCTYPE html>
<html lang="en">
<head>
<meta charset="utf-8">
<title>Harbour Lane Rentals – Price Packages</title>
<link href="https://fonts.googleapis.com/css2?family=Questrial&family=Roboto:wght@700&display=swap" rel="stylesheet">
<style>
:root{
  --backdrop:#2a2a2a;
  --sky:#2ec3ea;
  --sky-light:#6fd6f0;
  --teal:#2cb2d6;
  --teal-deep:#1a9dc0;
  --teal-dark:#14809f;
  --band:#16a3c5;
  --cell-label:#bfe7f4;
  --cell-label-alt:#a9ddee;
  --cell-value:#dcf3fa;
  --ink:#2f3a40;
  --white:#ffffff;
  --card-top:#ffffff;
  --card-bottom:#e3e6e8;
  --fold:#3b4650;
}
*{margin:0;padding:0;box-sizing:border-box}
html,body{width:1200px;height:864px;overflow:hidden;background:var(--backdrop)}
body{position:relative;font-family:"Questrial",sans-serif;color:var(--ink)}
.page{position:absolute;top:91px;width:546px;height:771px;transform:scale(.96);transform-origin:0 0;background:var(--teal);overflow:hidden}
.page--front{left:44px}
.page--back{left:625px}
.top-strip{position:absolute;left:0;top:0;width:100%;height:25px;background:linear-gradient(100deg,var(--sky-light) 0 44%,var(--sky) 44% 100%)}
.photo{position:absolute;left:0;top:25px;width:100%;height:343px}
.photo--homes{background:linear-gradient(180deg,#3f8fd6 0%,#8cc3ea 35%,#5d7b63 62%,#3a4a3c 100%)}
.photo--harbour{background:linear-gradient(180deg,#1f7fd2 0%,#6fb4ea 45%,#4f7d6a 55%,#1d6ea8 62%,#0f4f86 100%)}
.headline{position:absolute;left:40px;width:464px;top:288px;text-align:center;color:var(--white);font-weight:400;font-size:29px;line-height:34px;letter-spacing:.5px}
.brand{position:absolute;left:352px;top:18px;width:150px;height:70px;background:var(--sky);clip-path:polygon(0 0,100% 0,100% 72%,50% 100%,0 72%);color:var(--white);text-align:center;font-size:16px;line-height:17px;padding-top:10px}
.body{position:absolute;left:0;top:368px;width:100%;height:403px;background:linear-gradient(180deg,var(--teal) 0%,#3cbcdc 100%)}
.footer{position:absolute;left:0;top:748px;width:100%;height:23px;background:var(--teal-deep);color:var(--white)}
.footer .address{position:absolute;left:24px;top:4px;display:flex;align-items:center;gap:5px;font-size:12px;letter-spacing:-.2px;white-space:nowrap}
.footer .site{position:absolute;left:322px;top:5px;display:flex;align-items:center;gap:6px;font-size:12.5px;white-space:nowrap}
.email{position:absolute;left:322px;top:729px;color:var(--white);font-size:12.5px;display:flex;align-items:center;gap:6px;white-space:nowrap}
.card{position:absolute;left:25px;top:377px;width:275px;height:371px;background:linear-gradient(180deg,var(--card-top),var(--card-bottom))}
.fold{position:absolute;width:0;height:0;border-style:solid}
.fold--left{left:14px;top:725px;border-width:0 0 14px 11px;border-color:transparent transparent var(--fold) transparent;transform:scaleX(-1)}
.fold--right{left:300px;top:725px;border-width:0 0 14px 11px;border-color:transparent transparent var(--fold) transparent}
.card-title{position:absolute;left:25px;top:390px;width:275px;height:27px;background:var(--band);color:var(--white);font-weight:400;font-size:19px;line-height:27px;text-align:center;letter-spacing:.3px;white-space:nowrap}
.includes{position:absolute;left:42px;top:424px;font-size:20px;color:var(--teal-dark)}
.features{position:absolute;left:44px;top:451px;width:250px;list-style:none;font-size:11px;line-height:17.3px;color:var(--ink)}
.features li{position:relative;padding-left:20px}
.features li.multi{line-height:13px;padding-top:2px;padding-bottom:2px}
.features li svg{position:absolute;left:2px;top:4px}
.pricing-title{position:absolute;left:320px;top:404px;width:212px;font-weight:400;font-size:17px;color:var(--white);letter-spacing:.2px;white-space:nowrap}
.pricing{position:absolute;left:319px;top:430px;width:212px;table-layout:fixed;border-collapse:separate;border-spacing:0 1px;font-size:9.5px}
.pricing col.label-col{width:100px}
.pricing td{height:20.5px;padding:0 8px;vertical-align:middle;white-space:nowrap;overflow:hidden}
.pricing tr:first-child td{height:28px}
.pricing .label{background:var(--cell-label)}
.pricing .label--wrap{white-space:normal;line-height:11px}
.pricing tr:nth-child(even) .label{background:var(--cell-label-alt)}
.pricing .value{background:var(--cell-value);font-size:10.5px;padding-left:14px}
.pricing .value--small{font-size:9px}
.pricing .value small{display:block;font-size:7px;line-height:8px}
.pricing .value .big{font-size:13px;line-height:13px}
.contact-label{position:absolute;left:265px;top:650px;width:130px;height:18px;line-height:18px;transform:rotate(-90deg);transform-origin:center;color:var(--white);font-size:15px;letter-spacing:1.5px;text-align:center;white-space:nowrap}
.phone-card{position:absolute;left:357px;width:172px;height:44px;background:var(--white);border-radius:6px;text-align:right;padding:5px 10px 0 0}
.phone-card .name{display:block;font-size:13px;color:var(--teal-deep);line-height:14px;white-space:nowrap}
.phone-card .number{display:block;font-family:"Roboto",sans-serif;font-weight:700;font-size:20.5px;color:var(--teal-dark);line-height:24px;white-space:nowrap}
.phone-card--first{top:609px}
.phone-card--second{top:670px}
.phone-icon{position:absolute;left:349px;width:30px;height:30px}
.phone-icon--first{top:600px}
.phone-icon--second{top:661px}
</style>
</head>
<body>

<section class="page page--front">
  <div class="top-strip"></div>
  <div class="photo photo--homes" role="img" aria-label="Photo of modern terraced homes with gardens on a hillside under blue sky"></div>
  <h1 class="headline">PROPERTY MANAGEMENT<br>DONE RIGHT!</h1>
  <div class="brand">HARBOUR LANE<br>RENTALS</div>
  <div class="body"></div>
  <div class="card"></div>
  <span class="fold fold--left"></span><span class="fold fold--right"></span>
  <h2 class="card-title">ALL INCLUSIVE PACKAGE</h2>
  <p class="includes">Includes:</p>
  <ul class="features">
    <li><svg width="9" height="9" viewBox="0 0 10 10"><path d="M1 5l3 3 5-7" fill="none" stroke="#2cb2d6" stroke-width="1.6"/></svg>Securing Tenant</li>
    <li><svg width="9" height="9" viewBox="0 0 10 10"><path d="M1 5l3 3 5-7" fill="none" stroke="#2cb2d6" stroke-width="1.6"/></svg>Reference/Database Checking</li>
    <li><svg width="9" height="9" viewBox="0 0 10 10"><path d="M1 5l3 3 5-7" fill="none" stroke="#2cb2d6" stroke-width="1.6"/></svg>Lease Preparation and Signing</li>
    <li><svg width="9" height="9" viewBox="0 0 10 10"><path d="M1 5l3 3 5-7" fill="none" stroke="#2cb2d6" stroke-width="1.6"/></svg>Direct Debit rent collection</li>
    <li><svg width="9" height="9" viewBox="0 0 10 10"><path d="M1 5l3 3 5-7" fill="none" stroke="#2cb2d6" stroke-width="1.6"/></svg>Zero arrears policy management</li>
    <li><svg width="9" height="9" viewBox="0 0 10 10"><path d="M1 5l3 3 5-7" fill="none" stroke="#2cb2d6" stroke-width="1.6"/></svg>Payment of Rates and levies</li>
    <li><svg width="9" height="9" viewBox="0 0 10 10"><path d="M1 5l3 3 5-7" fill="none" stroke="#2cb2d6" stroke-width="1.6"/></svg>Insurance management</li>
    <li><svg width="9" height="9" viewBox="0 0 10 10"><path d="M1 5l3 3 5-7" fill="none" stroke="#2cb2d6" stroke-width="1.6"/></svg>Coordination or all repairs and maintenance</li>
    <li><svg width="9" height="9" viewBox="0 0 10 10"><path d="M1 5l3 3 5-7" fill="none" stroke="#2cb2d6" stroke-width="1.6"/></svg>Regular rent reviews and renewals</li>
    <li class="multi"><svg width="9" height="9" viewBox="0 0 10 10"><path d="M1 5l3 3 5-7" fill="none" stroke="#2cb2d6" stroke-width="1.6"/></svg>Detailed ingoing, ongoing and outgoing inspections with photos and videos – viewable through your personal Landlord portal</li>
    <li><svg width="9" height="9" viewBox="0 0 10 10"><path d="M1 5l3 3 5-7" fill="none" stroke="#2cb2d6" stroke-width="1.6"/></svg>Bond management – lodging and refunding</li>
    <li><svg width="9" height="9" viewBox="0 0 10 10"><path d="M1 5l3 3 5-7" fill="none" stroke="#2cb2d6" stroke-width="1.6"/></svg>Electronic monthly and EOFY statements</li>
    <li><svg width="9" height="9" viewBox="0 0 10 10"><path d="M1 5l3 3 5-7" fill="none" stroke="#2cb2d6" stroke-width="1.6"/></svg>Annual scheduled maintenance report</li>
    <li><svg width="9" height="9" viewBox="0 0 10 10"><path d="M1 5l3 3 5-7" fill="none" stroke="#2cb2d6" stroke-width="1.6"/></svg>Regulation/compliance management</li>
    <li><svg width="9" height="9" viewBox="0 0 10 10"><path d="M1 5l3 3 5-7" fill="none" stroke="#2cb2d6" stroke-width="1.6"/></svg>Tribunal Representation</li>
  </ul>
  <h2 class="pricing-title">ALL INCLUSIVE PACKAGE</h2>
  <table class="pricing">
    <colgroup><col class="label-col"><col></colgroup>
    <tr><td class="label">Management Rate:</td><td class="value"><span class="big">10% + GST</span><small>of rental income</small></td></tr>
    <tr><td class="label">Letting Fee:</td><td class="value">No Charge</td></tr>
    <tr><td class="label">Advertising:</td><td class="value">No Charge</td></tr>
    <tr><td class="label label--wrap">Professional Photography:</td><td class="value">$199 (inc GST)<small>4 x Photos</small></td></tr>
    <tr><td class="label">Statements:</td><td class="value">No Charge</td></tr>
    <tr><td class="label">Lease Preperation:</td><td class="value">No Charge</td></tr>
    <tr><td class="label">Renewal Fees:</td><td class="value">No Charge</td></tr>
  </table>
  <div class="contact-label">CONTACT INFO</div>
  <div class="phone-card phone-card--first"><span class="name">Tom Willard</span><span class="number">0438 216 907</span></div>
  <div class="phone-card phone-card--second"><span class="name">Marika Dunstan</span><span class="number">0419 572 046</span></div>
  <svg class="phone-icon phone-icon--first" viewBox="0 0 30 30"><circle cx="15" cy="15" r="14" fill="#1a9dc0" stroke="#fff" stroke-width="2"/><path d="M10 8c-1 1-1 3 0 5 2 4 4 6 8 8 2 1 4 1 5 0l-3-3-2 1c-2-1-3-3-4-4l1-2z" fill="#fff"/></svg>
  <svg class="phone-icon phone-icon--second" viewBox="0 0 30 30"><circle cx="15" cy="15" r="14" fill="#1a9dc0" stroke="#fff" stroke-width="2"/><path d="M10 8c-1 1-1 3 0 5 2 4 4 6 8 8 2 1 4 1 5 0l-3-3-2 1c-2-1-3-3-4-4l1-2z" fill="#fff"/></svg>
  <div class="email"><svg width="12" height="9" viewBox="0 0 12 9"><rect x=".5" y=".5" width="11" height="8" fill="none" stroke="#fff"/><path d="M.5.5l5.5 4 5.5-4" fill="none" stroke="#fff"/></svg>info@harbourlanerentals.com.au</div>
  <footer class="footer">
    <span class="address"><svg width="9" height="13" viewBox="0 0 9 13"><path d="M4.5 12.5S.5 7.5.5 4.5a4 4 0 0 1 8 0c0 3-4 8-4 8z" fill="none" stroke="#fff"/><circle cx="4.5" cy="4.5" r="1.5" fill="#fff"/></svg>Suite 7, 12-14 Carrow Parade, Dee Why NSW 2099</span>
    <span class="site"><svg width="11" height="11" viewBox="0 0 12 12"><circle cx="6" cy="6" r="5.5" fill="none" stroke="#fff"/><ellipse cx="6" cy="6" rx="2.5" ry="5.5" fill="none" stroke="#fff"/><path d="M.5 6h11" stroke="#fff"/></svg>www.harbourlanerentals.com.au</span>
  </footer>
</section>

<section class="page page--back">
  <div class="top-strip"></div>
  <div class="photo photo--harbour" role="img" aria-label="Photo of a Northern Beaches harbour with moored boats and a speedboat on blue water"></div>
  <div class="brand">HARBOUR LANE<br>RENTALS</div>
  <div class="body"></div>
  <div class="card"></div>
  <span class="fold fold--left"></span><span class="fold fold--right"></span>
  <h2 class="card-title">ALL INCLUSIVE PACKAGE</h2>
  <p class="includes">Includes:</p>
  <ul class="features">
    <li><svg width="9" height="9" viewBox="0 0 10 10"><path d="M1 5l3 3 5-7" fill="none" stroke="#2cb2d6" stroke-width="1.6"/></svg>Securing Tenant</li>
    <li><svg width="9" height="9" viewBox="0 0 10 10"><path d="M1 5l3 3 5-7" fill="none" stroke="#2cb2d6" stroke-width="1.6"/></svg>Reference/Database Checking</li>
    <li><svg width="9" height="9" viewBox="0 0 10 10"><path d="M1 5l3 3 5-7" fill="none" stroke="#2cb2d6" stroke-width="1.6"/></svg>Lease Preparation and Signing</li>
    <li><svg width="9" height="9" viewBox="0 0 10 10"><path d="M1 5l3 3 5-7" fill="none" stroke="#2cb2d6" stroke-width="1.6"/></svg>Direct Debit rent collection</li>
    <li><svg width="9" height="9" viewBox="0 0 10 10"><path d="M1 5l3 3 5-7" fill="none" stroke="#2cb2d6" stroke-width="1.6"/></svg>Zero arrears policy management</li>
    <li><svg width="9" height="9" viewBox="0 0 10 10"><path d="M1 5l3 3 5-7" fill="none" stroke="#2cb2d6" stroke-width="1.6"/></svg>Payment of Rates and levies</li>
    <li><svg width="9" height="9" viewBox="0 0 10 10"><path d="M1 5l3 3 5-7" fill="none" stroke="#2cb2d6" stroke-width="1.6"/></svg>Insurance management</li>
    <li><svg width="9" height="9" viewBox="0 0 10 10"><path d="M1 5l3 3 5-7" fill="none" stroke="#2cb2d6" stroke-width="1.6"/></svg>Coordination or all repairs and maintenance</li>
    <li><svg width="9" height="9" viewBox="0 0 10 10"><path d="M1 5l3 3 5-7" fill="none" stroke="#2cb2d6" stroke-width="1.6"/></svg>Regular rent reviews and renewals</li>
    <li class="multi"><svg width="9" height="9" viewBox="0 0 10 10"><path d="M1 5l3 3 5-7" fill="none" stroke="#2cb2d6" stroke-width="1.6"/></svg>Detailed ingoing, ongoing and outgoing inspections with photos and videos – viewable through your personal Landlord portal</li>
    <li><svg width="9" height="9" viewBox="0 0 10 10"><path d="M1 5l3 3 5-7" fill="none" stroke="#2cb2d6" stroke-width="1.6"/></svg>Bond management – lodging and refunding</li>
    <li><svg width="9" height="9" viewBox="0 0 10 10"><path d="M1 5l3 3 5-7" fill="none" stroke="#2cb2d6" stroke-width="1.6"/></svg>Electronic monthly and EOFY statements</li>
    <li><svg width="9" height="9" viewBox="0 0 10 10"><path d="M1 5l3 3 5-7" fill="none" stroke="#2cb2d6" stroke-width="1.6"/></svg>Annual scheduled maintenance report</li>
    <li><svg width="9" height="9" viewBox="0 0 10 10"><path d="M1 5l3 3 5-7" fill="none" stroke="#2cb2d6" stroke-width="1.6"/></svg>Regulation/compliance management</li>
    <li><svg width="9" height="9" viewBox="0 0 10 10"><path d="M1 5l3 3 5-7" fill="none" stroke="#2cb2d6" stroke-width="1.6"/></svg>Tribunal Representation</li>
  </ul>
  <h2 class="pricing-title">ALL INCLUSIVE PACKAGE</h2>
  <table class="pricing">
    <colgroup><col class="label-col"><col></colgroup>
    <tr><td class="label">Management Rate:</td><td class="value"><span class="big">6% + GST</span><small>of rental income</small></td></tr>
    <tr><td class="label">Letting Fee:</td><td class="value"><small>1 weeks rent + GST</small><small>6 or 12 month lease</small></td></tr>
    <tr><td class="label">Advertising:</td><td class="value">$350 (Inc GST)</td></tr>
    <tr><td class="label label--wrap">Professional Photography:</td><td class="value">$199 (inc GST)<small>4 x Photos</small></td></tr>
    <tr><td class="label">Statements:</td><td class="value">$5.00 Per month</td></tr>
    <tr><td class="label">Lease Preperation:</td><td class="value">No Charge</td></tr>
    <tr><td class="label">Renewal Fees:</td><td class="value value--small">½ Weeks Rent + GST</td></tr>
  </table>
  <div class="contact-label">CONTACT INFO</div>
  <div class="phone-card phone-card--first"><span class="name">Tom Willard</span><span class="number">0438 216 907</span></div>
  <div class="phone-card phone-card--second"><span class="name">Marika Dunstan</span><span class="number">0419 572 046</span></div>
  <svg class="phone-icon phone-icon--first" viewBox="0 0 30 30"><circle cx="15" cy="15" r="14" fill="#1a9dc0" stroke="#fff" stroke-width="2"/><path d="M10 8c-1 1-1 3 0 5 2 4 4 6 8 8 2 1 4 1 5 0l-3-3-2 1c-2-1-3-3-4-4l1-2z" fill="#fff"/></svg>
  <svg class="phone-icon phone-icon--second" viewBox="0 0 30 30"><circle cx="15" cy="15" r="14" fill="#1a9dc0" stroke="#fff" stroke-width="2"/><path d="M10 8c-1 1-1 3 0 5 2 4 4 6 8 8 2 1 4 1 5 0l-3-3-2 1c-2-1-3-3-4-4l1-2z" fill="#fff"/></svg>
  <div class="email"><svg width="12" height="9" viewBox="0 0 12 9"><rect x=".5" y=".5" width="11" height="8" fill="none" stroke="#fff"/><path d="M.5.5l5.5 4 5.5-4" fill="none" stroke="#fff"/></svg>info@harbourlanerentals.com.au</div>
  <footer class="footer">
    <span class="address"><svg width="9" height="13" viewBox="0 0 9 13"><path d="M4.5 12.5S.5 7.5.5 4.5a4 4 0 0 1 8 0c0 3-4 8-4 8z" fill="none" stroke="#fff"/><circle cx="4.5" cy="4.5" r="1.5" fill="#fff"/></svg>Suite 7, 12-14 Carrow Parade, Dee Why NSW 2099</span>
    <span class="site"><svg width="11" height="11" viewBox="0 0 12 12"><circle cx="6" cy="6" r="5.5" fill="none" stroke="#fff"/><ellipse cx="6" cy="6" rx="2.5" ry="5.5" fill="none" stroke="#fff"/><path d="M.5 6h11" stroke="#fff"/></svg>www.harbourlanerentals.com.au</span>
  </footer>
</section>

</body>
</html>
```